依頼詳細
買取対象はCD,DVD,本、ゲームソフト、ゲーム機本体です。デザインはファイル形式で送って頂き、
僕が受け取った後、すぐにでも看板制作会社及びビラ制作会社に依頼できるようにしてください。店舗の
写真を念のため添付しますので、イメージ作りに役立てて下さい。社名はホシノトレード ですので、
リサイクルの三角形のおなじみのマークは必ず看板及びチラシのデザインに含めて下さい。
記載項目
会社名、電話、メアド、ロゴ、コメント書き込み欄
希望イメージ
シンプル 複雑
単色 カラフル
暗い 明るい
日常 高級
遊び心 厳粛
未来的 伝統的
女性的 男性的
希望する色
納品ファイル
• 高解像度JPG (.jpg)
補足説明
金額を増やしました。よろしくお願いします。依頼内容について不明な点がありましたらなんなりとご質問下さい。
.
写真を添付しました。
店の名前は ホシノトレードです。 人通りの多い商店街に近い交差点の信号待ちの場所に近いところにオープンしますので、目につきやすい看板を希望しております。店の電話番号は決まっていますので、お仕事発注後にお伝えします。できれば発注後にメールで何回かのやり取りをさせて頂きたいと思っており、その点ご了承頂ける方に受注頂きたいと考えております。よろしくお願い致します。
選択させて頂いた提案物の著作権(財産権)等の扱いはTaskmill利用規約に従い、弊社に譲渡をお願いします。フォントや画像素材などを利用する場合は上記利用用途に使用できることを確認し、第三者の知的財産権等に注意してください

シンプルで気に入りました。

皆様ありがとうございました。またよろしくお願いします。

```html
<!DOCTYPE html>
<html lang="ja">
<head>
<meta charset="utf-8">
<title>ホシノトレード 高価買取</title>
<link rel="stylesheet" href="https://fonts.googleapis.com/css2?family=M+PLUS+1p:wght@500;800;900&family=Noto+Sans+JP:wght@500;700;900&display=swap">
<style>
  :root {
    --green: #3fae3a;
    --green-dark: #2b8a2a;
    --red: #e0141e;
    --red-dark: #9b0d12;
    --white: #ffffff;
    --ink: #1a1a1a;
    --grey: #555555;
  }
  * { box-sizing: border-box; margin: 0; padding: 0; }
  html, body { width: 833px; height: 1200px; overflow: hidden; background: var(--white); }
  .poster {
    position: relative; width: 833px; height: 1200px; overflow: hidden;
    background: var(--green);
    font-family: "M PLUS 1p", "Noto Sans JP", sans-serif;
  }
  .abs { position: absolute; }

  /* top icons */
  .format-badge { background: var(--white); border-radius: 6px; }
  .icon { fill: none; stroke: var(--white); stroke-width: 5; }

  .character {
    left: 470px; top: 0; width: 363px; height: 800px;
    background: linear-gradient(180deg, #f2c27c 0%, #f8e3cf 35%, #ffffff 60%, #5bb0d9 85%, #e94a58 100%);
    opacity: .92;
    border-bottom-left-radius: 180px;
  }

  .speech {
    left: 105px; top: 135px; width: 570px; height: 110px;
    background: var(--white); border-radius: 55px;
    display: flex; align-items: center; justify-content: center;
    font-family: "Noto Sans JP", sans-serif; font-weight: 900; font-size: 66px;
    color: var(--green-dark); letter-spacing: 2px;
  }
  .speech::after {
    content: ""; position: absolute; left: 250px; bottom: -34px;
    border-left: 26px solid transparent; border-right: 26px solid transparent;
    border-top: 36px solid var(--white);
  }

  /* headline */
  .headline-high {
    left: 50px; top: 360px; width: 135px; height: 215px;
    background: var(--red); border: 6px solid var(--white);
    display: flex; flex-direction: column; align-items: center; justify-content: center;
    color: var(--white); font-family: "Noto Sans JP", sans-serif; font-weight: 900;
    font-size: 92px; line-height: 1;
  }
  .headline-buy {
    left: 195px; top: 325px; width: 470px; height: 240px;
    background: var(--red); border: 6px solid var(--white);
    display: flex; align-items: center; justify-content: center;
    color: var(--white); font-family: "Noto Sans JP", sans-serif; font-weight: 900;
    font-size: 210px; line-height: 1; letter-spacing: -6px;
    text-shadow: 6px 6px 0 var(--red-dark);
  }
  .shop-name {
    left: 70px; top: 575px; width: 710px; height: 110px;
    background: var(--white); transform: rotate(-4deg);
    display: flex; align-items: center; justify-content: center;
    color: var(--red); font-family: "Noto Sans JP", sans-serif; font-weight: 900;
    font-size: 80px; letter-spacing: 2px;
    box-shadow: 0 6px 0 var(--green-dark);
  }

  /* lower block */
  .comment-box {
    left: 30px; top: 730px; width: 248px; height: 165px;
    border: 4px solid var(--white);
    color: var(--white); font-weight: 500; font-size: 30px; line-height: 1.35;
    padding: 22px 20px;
  }
  .items {
    left: 300px; top: 760px; width: 520px;
    color: var(--white); font-family: "Noto Sans JP", sans-serif; font-weight: 900;
    font-size: 58px; line-height: 1.2; letter-spacing: 1px;
  }
  .items li { list-style: none; display: flex; align-items: center; gap: 10px; }

  /* footer */
  .footer {
    left: 0; top: 1000px; width: 833px; height: 200px; background: var(--white);
  }
  .recycle-mark {
    left: 25px; top: 1030px; width: 140px; height: 140px; border-radius: 50%;
    background: var(--green);
  }
  .phone {
    left: 200px; top: 1015px; color: var(--ink);
    font-family: "Noto Sans JP", sans-serif; font-weight: 900; font-size: 70px; line-height: 1.1;
    display: flex; align-items: center; gap: 6px;
  }
  .email {
    left: 205px; top: 1105px; color: var(--ink); font-weight: 800; font-size: 34px; letter-spacing: 1px;
  }
  .hours {
    left: 205px; top: 1158px; width: 610px; color: var(--grey); font-weight: 800; font-size: 22px;
    display: flex; justify-content: space-between;
  }
</style>
</head>
<body>
<div class="poster">

  <div class="abs character" role="img" aria-label="制服姿のアニメ風の女の子のイラスト"></div>

  <!-- top format icons -->
  <div class="abs format-badge" style="left:30px;top:22px;width:120px;height:60px;" role="img" aria-label="ディスク規格マーク"></div>
  <svg class="abs" style="left:170px;top:18px" width="90" height="70" viewBox="0 0 90 70" aria-hidden="true">
    <path class="icon" d="M45 14 C32 6 14 6 6 10 V62 C14 58 32 58 45 66 C58 58 76 58 84 62 V10 C76 6 58 6 45 14 Z M45 14 V66"/>
  </svg>
  <svg class="abs" style="left:280px;top:12px" width="80" height="80" viewBox="0 0 80 80" aria-hidden="true">
    <circle cx="40" cy="40" r="34" fill="#fff"/><circle cx="40" cy="40" r="9" fill="var(--green)"/>
  </svg>

  <div class="abs speech">売ってください!</div>

  <svg class="abs" style="left:130px;top:270px" width="100" height="60" viewBox="0 0 100 60" aria-hidden="true">
    <rect x="4" y="8" width="92" height="44" rx="22" fill="#fff"/>
    <rect x="20" y="26" width="20" height="7" fill="var(--green)"/><rect x="26.5" y="19" width="7" height="21" fill="var(--green)"/>
    <circle cx="68" cy="24" r="5" fill="var(--green)"/><circle cx="78" cy="34" r="5" fill="var(--green)"/>
  </svg>
  <div class="abs format-badge" style="left:255px;top:255px;width:110px;height:70px;" role="img" aria-label="ディスク規格マーク"></div>

  <div class="abs headline-high"><span>高</span><span>価</span></div>
  <div class="abs headline-buy">買取</div>
  <div class="abs shop-name">ホシノトレード</div>

  <!-- lower icons -->
  <div class="abs format-badge" style="left:420px;top:705px;width:70px;height:45px;" role="img" aria-label="ディスク規格マーク"></div>
  <div class="abs format-badge" style="left:505px;top:705px;width:80px;height:45px;" role="img" aria-label="ディスク規格マーク"></div>
  <svg class="abs" style="left:600px;top:702px" width="60" height="50" viewBox="0 0 90 70" aria-hidden="true">
    <path class="icon" d="M45 14 C32 6 14 6 6 10 V62 C14 58 32 58 45 66 C58 58 76 58 84 62 V10 C76 6 58 6 45 14 Z M45 14 V66"/>
  </svg>

  <div class="abs comment-box">コメント<br>書き込み欄</div>

  <ul class="abs items">
    <li>CD・DVD・本</li>
    <li>ゲームソフト
      <svg width="56" height="56" viewBox="0 0 80 80" aria-hidden="true"><circle cx="40" cy="40" r="34" fill="#fff"/><circle cx="40" cy="40" r="9" fill="var(--green)"/></svg>
    </li>
    <li>
      <svg width="70" height="46" viewBox="0 0 100 60" aria-hidden="true">
        <rect x="4" y="8" width="92" height="44" rx="22" fill="#fff"/>
        <rect x="20" y="26" width="20" height="7" fill="var(--green)"/><rect x="26.5" y="19" width="7" height="21" fill="var(--green)"/>
        <circle cx="68" cy="24" r="5" fill="var(--green)"/><circle cx="78" cy="34" r="5" fill="var(--green)"/>
      </svg>ゲーム機本体
    </li>
  </ul>

  <!-- footer -->
  <div class="abs footer"></div>
  <div class="abs recycle-mark" role="img" aria-label="リサイクルマーク"></div>
  <div class="abs phone">
    <svg width="62" height="56" viewBox="0 0 62 56" aria-hidden="true">
      <path d="M4 22 C4 8 58 8 58 22 L50 28 L42 20 H20 L12 28 Z" fill="var(--ink)"/>
      <rect x="14" y="30" width="34" height="22" rx="4" fill="var(--ink)"/>
      <circle cx="31" cy="41" r="6" fill="#fff"/>
    </svg>
    <span>00-0000-0000</span>
  </div>
  <div class="abs email">○○○○○○○○○@○○○○○○</div>
  <div class="abs hours"><span>営業時間/00:00~00:00</span><span>定休日/○○○○</span></div>

</div>
</body>
</html>
```